Online plant nursery needs3 seperate slides for a intro web site slide slide show

We need 3 slide graphics / banners measurments should be 960wide 540 tall and 2mb or smaller. We are an online mail order nursery that focuses sales on Peonies.
Slide 1: Use faded out photos of Peony Garden with many flowers just budding. Our logo and the Words "A Lost Spring is Never Found Again". try to use our logo in a small small watermark on all slides.
Slide 2: Use your own creativity for the slide.... message should say "Free Shipping"
Slide 3: Use your own creativity for the slide .... messgae "Shop Our Other Items". To see site it will be used on go to http://k4830157.tbrwxq9pnlhe.preview82.shopnestle-example.com/

Target Market(s)

home owners age 30 - 65.

Industry/Entity Type

Nursery

Requirements
Must have
• must transition well.
Should not have
• can not be larger than 2MB per file

```html
<!DOCTYPE html>
<html lang="en">
<head>
<meta charset="utf-8">
<title>Peony Nursery Slides</title>
<link href="https://fonts.googleapis.com/css2?family=Cinzel:wght@400;500&display=swap" rel="stylesheet">
<style>
  :root {
    --page: #ffffff;
    --frame: #111111;
    --caption: #ffffff;
    --caption-shadow: rgba(0, 0, 0, 0.5);
    --mark: #8a2f4f;
    --mark-text: #6e2440;
    --garden-deep: #3f7a2e;
    --garden-mid: #6ea64e;
    --garden-light: #a8d08a;
    --garden-haze: #c9e2b4;
    --bud-pink: #b66a80;
    --bloom-pink: #f2a9c6;
    --bloom-rose: #e07aa9;
    --bloom-white: #fbf1f4;
    --bloom-lilac: #d9a2e2;
    --dew-sage: #8fa66b;
    --dew-olive: #6f8a4c;
    --dew-cream: #f3e6dc;
    --dew-rose: #cf6f82;
  }
  * { margin: 0; padding: 0; box-sizing: border-box; }
  html, body {
    width: 710px; height: 1200px; overflow: hidden; background: var(--page);
  }
  .slideshow { position: relative; width: 710px; height: 1200px; }
  .slide {
    position: absolute; left: 6px; width: 698px; height: 393px; overflow: hidden;
  }
  .slide--garden { top: 6px; }
  .slide--shipping { top: 401px; height: 394px; }
  .slide--shop { top: 799px; height: 392px; }
  .slide__photo { position: absolute; inset: 0; }
  .slide--garden .slide__photo {
    background:
      radial-gradient(ellipse 60% 55% at 25% 40%, rgba(182,106,128,0.28), transparent 70%),
      radial-gradient(ellipse 70% 60% at 80% 70%, rgba(182,106,128,0.22), transparent 70%),
      radial-gradient(ellipse 80% 60% at 70% 10%, var(--garden-haze), transparent 75%),
      linear-gradient(180deg, var(--garden-light) 0%, var(--garden-mid) 50%, var(--garden-deep) 100%);
  }
  .slide--shipping .slide__photo {
    background:
      radial-gradient(ellipse 55% 65% at 15% 25%, var(--bloom-pink), transparent 75%),
      radial-gradient(ellipse 55% 65% at 75% 20%, var(--bloom-lilac), transparent 75%),
      radial-gradient(ellipse 60% 60% at 60% 85%, var(--bloom-rose), transparent 75%),
      radial-gradient(ellipse 45% 55% at 95% 85%, var(--bloom-white), transparent 75%),
      radial-gradient(ellipse 55% 60% at 15% 90%, var(--bloom-pink), transparent 75%),
      linear-gradient(90deg, #f7dfe8, var(--bloom-white) 35%, #f3cfe0 70%, var(--bloom-white));
  }
  .slide--shop .slide__photo {
    background:
      radial-gradient(ellipse 50% 60% at 52% 35%, var(--dew-cream), transparent 80%),
      radial-gradient(ellipse 40% 35% at 60% 50%, var(--dew-rose), transparent 80%),
      radial-gradient(ellipse 55% 35% at 50% 90%, #4f6e32, transparent 80%),
      linear-gradient(180deg, var(--dew-sage), var(--dew-olive));
  }
  .caption-frame {
    position: absolute; left: 12px; right: 12px; top: 136px; height: 103px;
    border: 3px solid var(--frame);
    display: flex; align-items: center; justify-content: center;
  }
  .caption {
    font-family: "Cinzel", "Trajan Pro", serif;
    font-weight: 400;
    color: var(--caption);
    text-shadow: 1px 2px 3px var(--caption-shadow);
    white-space: nowrap;
    font-variant: small-caps;
  }
  .caption--tagline { font-size: 25px; letter-spacing: 0.33em; }
  .caption--shipping { font-size: 60px; letter-spacing: 0.37em; }
  .caption--shop { font-size: 40px; letter-spacing: 0.35em; }
  .brand-mark {
    position: absolute; right: 10px; bottom: 7px;
    display: flex; align-items: center; gap: 4px;
    font-family: "Cinzel", serif; font-size: 10px; font-weight: 500;
    color: var(--mark-text);
  }
  .brand-mark__dot {
    width: 14px; height: 14px; border-radius: 50%; background: var(--mark);
  }
</style>
</head>
<body>
<main class="slideshow">
  <section class="slide slide--garden">
    <div class="slide__photo" role="img" aria-label="Faded peony garden with many buds just opening among green leaves"></div>
    <div class="caption-frame"><p class="caption caption--tagline">A Lost Spring is Never Found Again</p></div>
    <div class="brand-mark"><span class="brand-mark__dot"></span>Bloomvale Peonies</div>
  </section>
  <section class="slide slide--shipping">
    <div class="slide__photo" role="img" aria-label="Collage of pink, lilac and white peony blooms in full flower"></div>
    <div class="caption-frame"><p class="caption caption--shipping">Free Shipping</p></div>
    <div class="brand-mark"><span class="brand-mark__dot"></span>Bloomvale Peonies</div>
  </section>
  <section class="slide slide--shop">
    <div class="slide__photo" role="img" aria-label="Close-up of a dew-covered pink and cream peony bud on a soft green background"></div>
    <div class="caption-frame"><p class="caption caption--shop">Shop Our Other Items</p></div>
    <div class="brand-mark"><span class="brand-mark__dot"></span>Bloomvale Peonies</div>
  </section>
</main>
</body>
</html>
```